Podiatry clinic requires a modern revamp and editing of existing website.

I would like a fresh new look and updated information for my current business website. An easy to navigate site with prominent address and phone number for call to action. We are a podiatry clinic that focuses on general and sports podiatry.
I would like 4 pages; including Home page, About Us, Services & Contact.
www.harbourlanefootcare.com

Target Market(s)

Active working professionals.

Industry/Entity Type

Medical

Coding

Coded - Design and coding required

Number of Pages Required

4 page

Font styles to use
Sans Serif

Colors
6b449b

Requirements
Must have
• A modern look with logo and active images; clean and uncluttered. Visible phone number and address for call to action.
• 4 pages - Home, About Us, Services, Contact.
• Home page - update address & service logos.
• About Us - update of personal information.
• Services - Revamp of existing page.
• Contact page to include Google map, email & phone number.
Nice to have
• Ability to add content easily; eg. a blog or adding video onto Home page.
• Link to Facebook page.

```html
<!DOCTYPE html>
<html lang="en">
<head>
<meta charset="utf-8">
<title>Harbour Lane Foot Care</title>
<link href="https://fonts.googleapis.com/css2?family=Lato:wght@400;700&family=Montserrat:wght@500;600&family=Raleway:wght@300;400;700&display=swap" rel="stylesheet">
<style>
:root{
  --purple:#4a2c91;
  --purple-soft:#9c86c9;
  --btn:#8a73bd;
  --ink:#222;
  --text:#444;
  --muted:#777;
  --line:#cfcfcf;
  --footer:#3a3a3a;
  --footer-line:#555;
  --copy:#262626;
  --white:#fff;
}
*{box-sizing:border-box;margin:0;padding:0}
html,body{width:712px;height:1200px;overflow:hidden;background:var(--white)}
body{position:relative;font-family:'Lato',sans-serif;color:var(--text)}
.abs{position:absolute}

.topbar{left:0;top:0;width:712px;height:18px;background:var(--purple);color:var(--white);font-size:8px}
.topbar .social{position:absolute;top:5px;width:8px;height:8px;border-radius:2px;background:rgba(255,255,255,.85)}
.topbar .contact-chip{position:absolute;top:0;height:18px;display:flex;align-items:center;gap:6px}
.topbar .icon-box{width:18px;height:18px;background:#1c1c1c;display:flex;align-items:center;justify-content:center}

.header{left:0;top:18px;width:712px;height:63px;background:var(--white)}
.brand{position:absolute;left:58px;top:12px;display:flex;align-items:center;gap:6px}
.brand .dot{width:14px;height:14px;border-radius:50%;background:var(--purple)}
.brand .name{font-family:'Lato',sans-serif;font-weight:700;font-size:13px;line-height:14px;color:var(--purple);width:90px}
.nav{position:absolute;left:297px;top:18px;display:flex;align-items:center;font-size:8px;color:var(--purple)}
.nav a{color:inherit;text-decoration:none;display:block;padding:0 12px;line-height:26px}
.nav a.active{border:1px solid var(--purple);font-weight:700;width:51px;text-align:center;padding:0;margin-right:1px}
.book{position:absolute;left:534px;top:18px;width:120px;height:25px;background:var(--purple);color:var(--white);font-family:'Montserrat',sans-serif;font-weight:500;font-size:8.5px;display:flex;align-items:center;gap:7px;padding-left:9px}

.hero{left:0;top:81px;width:712px;height:280px;background:linear-gradient(160deg,#a9a9a9 0%,#6e6e6e 40%,#3a3a3c 70%,#565a60 100%)}
.hero .arrow{position:absolute;top:132px;width:15px;height:15px;border:1px solid var(--white);border-radius:2px;display:flex;align-items:center;justify-content:center}
.hero h1{position:absolute;left:0;width:712px;top:246px;text-align:center;color:var(--white);font-family:'Lato',sans-serif;font-weight:700;font-size:18px}

.section-title{position:absolute;left:0;width:712px;text-align:center;font-family:'Raleway',sans-serif;font-weight:300;color:var(--ink)}
.section-title strong{font-weight:700;color:var(--purple)}
.rule{position:absolute;height:1px;background:var(--line)}

.welcome-text{left:92px;top:433px;width:528px;text-align:center;font-size:8.2px;line-height:14.5px;color:var(--text)}

.services{left:0;top:550px;width:712px;height:237px;background:linear-gradient(180deg,#4a4644 0%,#2e2b29 60%,#4d4540 100%)}
.card{position:absolute;top:68px;width:289px;height:119px;background:var(--white);border-radius:4px;overflow:hidden;display:flex}
.card .photo{width:148px;height:119px;flex:none}
.card .body{padding:8px 6px 0 6px}
.card h3{font-family:'Montserrat',sans-serif;font-weight:600;font-size:13.5px;color:var(--ink)}
.card h4{font-weight:700;font-size:7.5px;color:var(--ink);margin-top:4px}
.card p{font-size:7.6px;line-height:13px;color:var(--muted);margin-top:6px}
.card .more{display:inline-block;margin-top:7px;width:59px;height:19px;line-height:19px;text-align:center;background:var(--btn);color:var(--white);font-size:7.6px;font-weight:700}

.quote-mark{font-family:Georgia,serif;font-size:60px;color:#c8c8c8;line-height:1}
.review-text{left:130px;top:860px;width:452px;text-align:center;font-size:8.2px;line-height:14.5px;color:var(--text)}
.reviewer{left:0;width:712px;top:910px;text-align:center;font-size:9px;font-weight:700;color:var(--purple-soft)}
.avatar{position:absolute;width:40px;height:40px;border-radius:50%;top:942px}
.avatar.active{width:56px;height:56px;top:934px;border:2px solid var(--purple)}

.footer{left:0;top:1026px;width:712px;height:148px;background:var(--footer);color:#eee}
.footer h5{position:absolute;top:32px;font-family:'Montserrat',sans-serif;font-weight:600;font-size:8.5px;color:var(--white)}
.footer .underline{position:absolute;top:50px;height:1px;background:var(--footer-line)}
.footer .divider{position:absolute;top:16px;width:1px;height:118px;background:#2c2c2c}
.links{position:absolute;left:58px;top:56px;width:72px;list-style:none;font-size:7px}
.links li{height:20px;line-height:20px;border-bottom:1px solid var(--footer-line);padding-left:8px;position:relative}
.links li:last-child{border:none}
.links li::before{content:"";position:absolute;left:1px;top:7px;border-left:3px solid #eee;border-top:3px solid transparent;border-bottom:3px solid transparent}
.details{position:absolute;left:190px;top:56px;width:110px;font-size:7px;line-height:11px}
.details .row{display:flex;gap:6px;padding:4px 0;border-bottom:1px solid var(--footer-line)}
.details .row:last-child{border:none}
.map{position:absolute;left:368px;top:53px;width:134px;height:66px;background:linear-gradient(135deg,#dcdcd2,#c9cfc6 60%,#e8e0a0 100%)}
.footer-brand{position:absolute;left:564px;top:56px;display:flex;align-items:center;gap:5px}
.footer-brand .dot{width:12px;height:12px;border-radius:50%;background:#8a8a8a}
.footer-brand .name{font-weight:700;font-size:11px;line-height:13px;color:#8a8a8a;width:80px}
.copyright{left:0;top:1174px;width:712px;height:26px;background:var(--copy);color:#ddd;font-size:8px;text-align:center;line-height:26px}
.copyright strong{color:var(--white)}
</style>
</head>
<body>

<div class="abs topbar">
  <span class="social" style="left:342px"></span>
  <span class="social" style="left:362px"></span>
  <span class="social" style="left:383px"></span>
  <span class="social" style="left:406px"></span>
  <div class="contact-chip" style="left:428px">
    <span class="icon-box"><svg width="8" height="8" viewBox="0 0 10 10"><path d="M2 1l2 2-1 1.5c.6 1.2 1.3 1.9 2.5 2.5L7 6l2 2-1.3 1.5C4.5 9 1 5.5.5 2.3z" fill="#fff"/></svg></span>
    <span>555-014-2290</span>
  </div>
  <div class="contact-chip" style="left:516px">
    <span class="icon-box"><svg width="9" height="7" viewBox="0 0 10 8"><rect x="0" y="0" width="10" height="8" fill="#fff"/><path d="M0 0l5 4 5-4" stroke="#1c1c1c" fill="none"/></svg></span>
    <span>hello@harbourlanefootcare.com</span>
  </div>
</div>

<header class="abs header">
  <div class="brand"><span class="dot"></span><span class="name">Harbour Lane Foot Care</span></div>
  <nav class="nav">
    <a class="active" href="#">Home</a>
    <a href="#">About Us</a>
    <a href="#">Services</a>
    <a href="#">Contact</a>
  </nav>
  <div class="book">
    <svg width="12" height="12" viewBox="0 0 12 12"><circle cx="6" cy="3" r="2.5" fill="#fff"/><path d="M1 12c0-4 2-6 5-6s5 2 5 6z" fill="#fff"/></svg>
    Book Appointment
  </div>
</header>

<section class="abs hero" role="img" aria-label="Runner's feet on a treadmill with a highlighted ankle joint">
  <span class="arrow" style="left:36px"><svg width="8" height="6" viewBox="0 0 8 6"><path d="M8 3H1M3 1L1 3l2 2" stroke="#fff" fill="none"/></svg></span>
  <span class="arrow" style="left:660px"><svg width="8" height="6" viewBox="0 0 8 6"><path d="M0 3h7M5 1l2 2-2 2" stroke="#fff" fill="none"/></svg></span>
  <h1>Harbour Lane Foot Care is a Podiatry clinic in the heart of Melbourne</h1>
</section>

<h2 class="section-title" style="top:390px;font-size:22px">Welcome to <strong>Harbour Lane Foot Care</strong></h2>
<div class="rule" style="left:165px;width:382px;top:421px"></div>
<p class="abs welcome-text">Harbour Lane Foot Care is a Podiatry clinic in the heart of Melbourne CBD. We are located between Quay &amp; Marlow Streets in the Bayside Business Centre / Quay Hotel Complex.<br>Our podiatrists are fully qualified health professionals who are able to diagnose, treat, manage or help to prevent all medical conditions that affect the feet and lower limb.<br>We provide General Podiatry Treatment and some Specialised Services in relation to various foot conditions, including Sports Injuries, Orthotic Therapy and Nail Surgery.</p>

<section class="abs services">
  <h2 class="section-title" style="top:20px;font-size:21px;color:var(--white)">Our Services</h2>
  <div class="rule" style="left:265px;width:182px;top:52px;background:#8a8683"></div>
  <article class="card" style="left:58px">
    <div class="photo" role="img" aria-label="Podiatrist treating a patient's foot" style="background:linear-gradient(135deg,#e9dcd2,#c9a892 60%,#6f9ac9)"></div>
    <div class="body">
      <h3>General Podiatry</h3>
      <h4>Lorem Ipsum is simply dummy tex</h4>
      <p>When an unknown printer took a galley of type and scrambled it to make a type specimen book.</p>
      <span class="more">Read More</span>
    </div>
  </article>
  <article class="card" style="left:365px">
    <div class="photo" role="img" aria-label="Therapist assessing an athlete's leg" style="background:linear-gradient(135deg,#eef1f4,#c8cdd3 55%,#7c6a5d)"></div>
    <div class="body">
      <h3>Sports Podiatry</h3>
      <h4>Lorem Ipsum is simply dummy tex</h4>
      <p>When an unknown printer took a galley of type and scrambled it to make a type specimen book.</p>
      <span class="more">Read More</span>
    </div>
  </article>
</section>

<h2 class="section-title" style="top:806px;font-size:22px">Customer <strong>Review</strong></h2>
<div class="rule" style="left:165px;width:382px;top:844px"></div>
<span class="abs quote-mark" style="left:96px;top:852px">&ldquo;</span>
<span class="abs quote-mark" style="left:588px;top:862px">&rdquo;</span>
<p class="abs review-text">Fusce elementum, nulla vel pellentes consequat, ante nulla hendrerit arcu, ac tincidunt mauris lacus sed leo. vamus suscipit molestie vestibulum. Lorem ipsum dolor sit amet, Fusce elementum, nulla vel pellentes consequat, ante nulla hendrerit arcu, ac tincidunt mauris lacus sed leo. vamus suscipit molestie. Fusce elementum, nulla vel</p>
<p class="abs reviewer">Mr. Lorem Ipsum</p>
<div class="avatar" role="img" aria-label="Customer portrait" style="left:217px;background:#c9a58f"></div>
<div class="avatar" role="img" aria-label="Customer portrait" style="left:273px;background:#b39683"></div>
<div class="avatar active" role="img" aria-label="Customer portrait" style="left:329px;background:#d6c2b4"></div>
<div class="avatar" role="img" aria-label="Customer portrait" style="left:401px;background:#a77a62"></div>
<div class="avatar" role="img" aria-label="Customer portrait" style="left:457px;background:#b89a84"></div>

<footer class="abs footer">
  <span class="divider" style="left:162px"></span>
  <span class="divider" style="left:338px"></span>
  <span class="divider" style="left:534px"></span>

  <h5 style="left:58px">Quick Links</h5>
  <span class="underline" style="left:58px;width:72px"></span>
  <ul class="links"><li>Home</li><li>About Us</li><li>Services</li><li>Contact</li></ul>

  <h5 style="left:190px">Contact Details</h5>
  <span class="underline" style="left:190px;width:110px"></span>
  <div class="details">
    <div class="row"><svg width="6" height="8" viewBox="0 0 6 8"><path d="M3 0a3 3 0 013 3c0 2-3 5-3 5S0 5 0 3a3 3 0 013-3z" fill="#eee"/></svg><span>Suite 204 / 118 Harbour Lane<br>Melbourne&nbsp; 3000</span></div>
    <div class="row" style="padding:7px 0"><svg width="7" height="7" viewBox="0 0 10 10"><path d="M2 1l2 2-1 1.5c.6 1.2 1.3 1.9 2.5 2.5L7 6l2 2-1.3 1.5C4.5 9 1 5.5.5 2.3z" fill="#eee"/></svg><span>1300 555 014</span></div>
    <div class="row" style="padding:7px 0"><svg width="7" height="6" viewBox="0 0 10 8"><rect width="10" height="8" fill="#eee"/><path d="M0 0l5 4 5-4" stroke="#3a3a3a" fill="none"/></svg><span>info@harbourlanefootcare.com</span></div>
  </div>

  <h5 style="left:368px">Location Map</h5>
  <span class="underline" style="left:368px;width:134px"></span>
  <div class="map" role="img" aria-label="Street map showing the clinic location"></div>

  <div class="footer-brand"><span class="dot"></span><span class="name">Harbour Lane Foot Care</span></div>
</footer>

<div class="abs copyright">Copyright © 2016 <strong>Harbour Lane Foot Care</strong>. All Rights Reserved.</div>

</body>
</html>
```